UI/UX Design for AI Photo-to-Video Web Platform (Figma)

I am looking for a modern, high-converting redesign for my Next.js-based web platform. The service allows users to transform old photos into vibrant memories using AI. The design needs to be clean, intuitive, and "mobile-ready" (responsive).
Key Features to Visualize on the Homepage:
Photo Restoration & Colorization: A clear "before/after" visual showing a black-and-white photo turning into a high-quality color photo.
Photo-to-Video Animation: A visual representation of how both B&W and color photos are transformed into dynamic video clips.
Story Creation: A section showing how these photos and videos are combined into a single "Story Video" with background music.
Scope of Work:
Homepage Redesign: A hero section with the core value proposition and a visual walkthrough of the process.
Service/Internal Pages: Redesigning the functional pages where users upload files and manage their projects.
Responsive Design: While the focus is desktop, the layout must be designed with a "Mobile-First" mindset for easy porting to a mobile app later.
Technical Requirements for the Designer:
Tool: Must be designed in Figma.
Structure: Use Figma Auto Layout and Components for all elements (buttons, inputs, cards).
Design System: Provide a clear style guide (Typography, Color Palette, Spacing).
Assets: All icons should be in SVG format.
Style Preference:
Modern, sleek, and trustworthy.
Since the product is about "memories," the vibe should be emotional yet technologically advanced (AI-driven).

```html
<!DOCTYPE html>
<html lang="en">
<head>
<meta charset="utf-8">
<title>hueback.ai — Ai Photo and Video Enhancer</title>
<link href="https://fonts.googleapis.com/css2?family=Poppins:wght@400;500;600;700&display=swap" rel="stylesheet">
<style>
  :root {
    --orange: #d8850c;
    --orange-soft: #fdf4e6;
    --orange-line: #e8b36a;
    --hero-start: #a66b1b;
    --hero-end: #e3a845;
    --ink: #1c1c1c;
    --muted: #7a7a7a;
    --body-text: #4a4a4a;
    --green-ink: #0f2a1b;
    --line: #ececec;
    --white: #ffffff;
    --page: #ffffff;
  }
  * { box-sizing: border-box; margin: 0; padding: 0; }
  html, body { width: 733px; height: 1200px; overflow: hidden; }
  body { background: var(--page); font-family: "Poppins", sans-serif; color: var(--ink); position: relative; }

  .site-header { position: absolute; left: 0; top: 0; width: 733px; height: 30px; display: flex; align-items: center; justify-content: space-between; padding: 0 32px; border-bottom: 1px solid var(--line); }
  .brand { font-size: 12px; font-weight: 600; color: var(--ink); }
  .account { display: flex; align-items: center; gap: 16px; font-size: 5.5px; font-weight: 500; }
  .account-item { display: flex; align-items: center; gap: 4px; }
  .account-item .dim { color: var(--muted); font-weight: 400; }
  .dot { width: 8px; height: 8px; border-radius: 50%; background: var(--orange); }
  .chip { width: 8px; height: 6px; border-radius: 1.5px; background: var(--orange-line); }
  .avatar { width: 11px; height: 11px; border-radius: 50%; background: #8a8f96; }
  .caret { width: 0; height: 0; border-left: 2.5px solid transparent; border-right: 2.5px solid transparent; border-top: 3px solid #999; }

  .hero { position: absolute; left: 0; top: 30px; width: 733px; height: 198px; background: linear-gradient(100deg, var(--hero-start), var(--hero-end)); text-align: center; color: var(--white); }
  .hero h1 { margin-top: 20px; font-size: 31px; font-weight: 700; letter-spacing: -0.2px; line-height: 1.2; }
  .hero p { margin: 8px auto 0; width: 330px; font-size: 6.6px; line-height: 1.45; opacity: 0.95; }
  .mode-tabs { margin: 16px auto 0; width: 152px; height: 22px; border-radius: 11px; background: rgba(255,255,255,0.18); border: 1px solid rgba(255,255,255,0.35); display: flex; align-items: center; justify-content: space-between; padding: 0 3px; font-size: 6px; font-weight: 500; }
  .tab { display: flex; align-items: center; gap: 4px; padding: 0 5px; height: 16px; border-radius: 8px; white-space: nowrap; }
  .tab.active { background: var(--orange-soft); color: var(--orange); }
  .tab svg { width: 8px; height: 8px; }

  .upload-card { position: absolute; left: 76px; top: 185px; width: 547px; height: 278px; background: var(--white); border-radius: 9px; box-shadow: 0 4px 18px rgba(0,0,0,0.08); }
  .compare { position: absolute; left: 20px; top: 20px; width: 244px; height: 184px; border-radius: 7px; overflow: hidden; display: flex; }
  .compare .before { width: 122px; height: 100%; background: linear-gradient(160deg, #c9c9c6, #6d6d6a 60%, #3c3c3a); }
  .compare .after { width: 122px; height: 100%; background: linear-gradient(160deg, #e6c48a, #c2742b 40%, #2c3356 75%, #7a5a40); border-left: 1px solid var(--white); }
  .compare-label { position: absolute; bottom: 8px; font-size: 6px; font-weight: 600; color: var(--white); background: rgba(0,0,0,0.35); padding: 2px 6px; border-radius: 4px; }
  .compare-label.left { left: 8px; }
  .compare-label.right { right: 8px; }
  .compare-handle { position: absolute; left: 107px; top: 77px; width: 30px; height: 30px; border-radius: 50%; background: rgba(90,90,90,0.75); display: flex; align-items: center; justify-content: center; }

  .dropzone { position: absolute; left: 283px; top: 20px; width: 243px; height: 184px; border-radius: 7px; background: var(--orange-soft); padding: 11px; }
  .dropzone-inner { width: 100%; height: 100%; border: 1px dashed var(--orange-line); border-radius: 5px; text-align: center; padding-top: 19px; }
  .file-icon { width: 33px; height: 33px; margin: 0 auto; display: block; }
  .dropzone h2 { margin-top: 10px; font-size: 9px; font-weight: 500; }
  .dropzone small { display: block; margin: 3px auto 0; width: 200px; font-size: 5px; color: var(--muted); line-height: 1.5; }
  .btn-select { margin: 12px auto 0; width: 91px; height: 23px; border-radius: 12px; background: var(--orange); color: var(--white); font-size: 6px; font-weight: 600; display: flex; align-items: center; justify-content: center; gap: 6px; }

  .terms { position: absolute; left: 0; top: 218px; width: 100%; text-align: center; font-size: 5.6px; color: var(--muted); }
  .terms b { color: var(--orange); font-weight: 600; }
  .card-divider { position: absolute; left: 20px; right: 20px; top: 239px; height: 1px; background: var(--line); }
  .perks { position: absolute; left: 0; top: 252px; width: 100%; display: flex; justify-content: center; gap: 50px; font-size: 6.6px; font-weight: 500; }
  .perk { display: flex; align-items: center; gap: 6px; }
  .perk svg { width: 9px; height: 9px; }

  .how { position: absolute; left: 0; top: 504px; width: 733px; text-align: center; }
  .how h2 { font-size: 28px; font-weight: 700; color: var(--green-ink); }
  .steps { position: absolute; left: 76px; top: 53px; display: flex; gap: 16px; text-align: left; }
  .step { width: 183px; height: 172px; border: 1px solid var(--line); border-radius: 7px; padding: 0 11px; position: relative; }
  .step .step-art { position: absolute; left: 59px; top: 12px; width: 64px; height: 58px; border-radius: 12px; background: linear-gradient(150deg, #fbd77f, #eea63a); }
  .step .step-label { margin-top: 88px; font-size: 5.6px; color: var(--orange); font-weight: 500; }
  .step .step-title { margin-top: 4px; font-size: 10px; font-weight: 600; color: var(--green-ink); white-space: nowrap; }
  .step .step-desc { margin-top: 7px; font-size: 6px; line-height: 1.6; color: var(--body-text); }
  .step.offset .step-label { margin-top: 100px; }
</style>
</head>
<body>
  <header class="site-header">
    <div class="brand">hueback.ai</div>
    <div class="account">
      <div class="account-item"><span class="dot"></span>4740 credits</div>
      <div class="account-item"><span class="chip"></span>114MB <span class="dim">/ 1.0 GB</span></div>
      <div class="account-item"><span class="avatar"></span>Mara Lind <span class="caret"></span></div>
    </div>
  </header>

  <section class="hero">
    <h1>Ai Photo and Video Enhancer</h1>
    <p>Give your photos more depth and texture by using our AI. More natural tones and details will be apparent without the overly processed appearance.</p>
    <nav class="mode-tabs">
      <span class="tab active"><svg viewBox="0 0 10 10"><rect x="0.5" y="0.5" width="9" height="9" rx="2" fill="currentColor"/><path d="M1.5 8 L4 5 L6 7 L8 4.5 L8.5 8Z" fill="#fff"/></svg>Images</span>
      <span class="tab"><svg viewBox="0 0 10 10"><rect x="0.5" y="1.5" width="9" height="8" rx="1.5" fill="#fff"/><path d="M4 4 L7 5.5 L4 7Z" fill="#c58a2e"/></svg>Video Animations</span>
      <span class="tab"><svg viewBox="0 0 10 10"><circle cx="5" cy="5" r="4.5" fill="#fff"/><circle cx="5" cy="5" r="1.6" fill="#c58a2e"/></svg>Studio</span>
    </nav>
  </section>

  <section class="upload-card">
    <div class="compare">
      <div class="before" role="img" aria-label="Black-and-white archive photo of a man holding a child"></div>
      <div class="after" role="img" aria-label="The same archive photo restored in full colour"></div>
      <span class="compare-label left">Before</span>
      <span class="compare-label right">After</span>
      <div class="compare-handle">
        <svg width="12" height="8" viewBox="0 0 12 8"><path d="M4 0 L0 4 L4 8Z M8 0 L12 4 L8 8Z" fill="#fff"/></svg>
      </div>
    </div>

    <div class="dropzone">
      <div class="dropzone-inner">
        <svg class="file-icon" viewBox="0 0 33 33"><path d="M6 2 H21 L28 9 V30 a1 1 0 0 1 -1 1 H6 a1 1 0 0 1 -1 -1 V3 a1 1 0 0 1 1 -1Z" fill="#fff" stroke="#d9d9d9"/><path d="M21 2 V9 H28" fill="none" stroke="#d9d9d9"/><rect x="10" y="13" width="13" height="11" rx="1.5" fill="#f2a53a"/><path d="M11 23 L15 17 L18 21 L20 18.5 L22 23Z" fill="#fff"/></svg>
        <h2>Drag and drop images here</h2>
        <small>Maximum 20 images • 100MB total • JPG, PNG, GIF, TIFF up to 10MB each</small>
        <div class="btn-select">Select files
          <svg width="8" height="8" viewBox="0 0 8 8"><path d="M1 1 H7 M4 7 V3 M2 4.5 L4 2.5 L6 4.5" stroke="#fff" stroke-width="1" fill="none"/></svg>
        </div>
      </div>
    </div>

    <p class="terms">By uploading a file, you agree to our <b>Terms of Use</b> and <b>Privacy Policy</b>.</p>
    <div class="card-divider"></div>
    <div class="perks">
      <span class="perk"><svg viewBox="0 0 10 10"><path d="M5 0.7 L9 2.2 V5 C9 7.5 7 8.8 5 9.4 C3 8.8 1 7.5 1 5 V2.2Z" fill="none" stroke="#d8850c"/><path d="M3.3 5 L4.5 6.2 L6.8 3.8" fill="none" stroke="#d8850c"/></svg>Focused on privacy</span>
      <span class="perk"><svg viewBox="0 0 10 10"><rect x="0.8" y="0.8" width="8.4" height="8.4" rx="2" fill="none" stroke="#d8850c"/><path d="M3 6 Q5 8 7 6" fill="none" stroke="#d8850c"/></svg>User-friendly</span>
      <span class="perk"><svg viewBox="0 0 10 10"><path d="M5.5 0.8 L2.5 5.5 H5 L4.5 9.2 L7.5 4.5 H5Z" fill="none" stroke="#d8850c"/></svg>Fast and accurate</span>
    </div>
  </section>

  <section class="how">
    <h2>How It Works</h2>
    <div class="steps">
      <article class="step">
        <div class="step-art" role="img" aria-label="Illustration of a browser window with a hand selecting an option"></div>
        <p class="step-label">Step 1</p>
        <h3 class="step-title">Select enhancement type</h3>
        <p class="step-desc">Lorem ipsum dolor sit amet consectetur. Nec sollicitudin dignissim enim neque habitant.</p>
      </article>
      <article class="step">
        <div class="step-art" role="img" aria-label="Illustration of a cloud with an upload arrow"></div>
        <p class="step-label">Step 2</p>
        <h3 class="step-title">Upload files</h3>
        <p class="step-desc">Facilisis quis tempus sit eget egestas sagittis sed. Mollis eget viverra feugiat diam et aliquet tellus.</p>
      </article>
      <article class="step offset">
        <div class="step-art" role="img" aria-label="Illustration of a sparkling file with a download arrow"></div>
        <p class="step-label">Step 3</p>
        <h3 class="step-title">Download results</h3>
        <p class="step-desc">Malesuada tempus vitae tellus fermentum posuere lectus scelerisque.</p>
      </article>
    </div>
  </section>
</body>
</html>
```